Stationery for a Messianic Congregation
Business Envelopes, Cards, Letterhead
Professional
Gregory T. Morrow
Ro'i
5142 Callaway Lane Orlando, FL 32867
gmorrow@ohelnoam.com
www.ohelnoam.com
Worship - Study - Fellowship

```html
<!DOCTYPE html>
<html lang="en">
<head>
<meta charset="utf-8">
<title>Ohel Noam Stationery</title>
<link href="https://fonts.googleapis.com/css2?family=Cinzel:wght@500&family=Lato:wght@400;700&display=swap" rel="stylesheet">
<style>
  :root {
    --stage: #9b9b9b;
    --paper: #ffffff;
    --charcoal: #58585a;
    --charcoal-dark: #4a4a4c;
    --gold: #f0b800;
    --gold-deep: #b98a12;
    --ink: #4d4d4f;
    --map-road: #8c8c8e;
    --hole: #b9b9bb;
  }
  * { margin: 0; padding: 0; box-sizing: border-box; }
  html, body { width: 1200px; height: 806px; overflow: hidden; }
  body { background: var(--stage); position: relative; font-family: "Lato", sans-serif; color: var(--ink); }

  .piece { position: absolute; overflow: hidden; box-shadow: 0 2px 6px rgba(0,0,0,.25); }
  .wave { position: absolute; left: 0; width: 100%; display: block; }

  .brand { position: absolute; display: flex; flex-direction: column; align-items: flex-start; }
  .brand-row { display: flex; align-items: center; gap: 5px; }
  .brand-dot { border-radius: 50%; background: var(--gold); flex: none; }
  .brand-name { font-family: "Cinzel", serif; font-weight: 500; color: var(--charcoal); letter-spacing: .04em; line-height: 1; }
  .brand-sub { font-family: "Lato", sans-serif; color: var(--gold-deep); letter-spacing: .06em; white-space: nowrap; }
  .brand-tag { font-family: "Lato", sans-serif; color: var(--gold-deep); letter-spacing: .04em; white-space: nowrap; }

  /* Letterhead */
  .letterhead { left: 60px; top: 19px; width: 458px; height: 739px; background: var(--paper); }
  .letterhead .brand { left: 26px; top: 30px; }
  .letterhead .brand-dot { width: 16px; height: 16px; }
  .letterhead .brand-name { font-size: 19px; }
  .letterhead .brand-sub { font-size: 7px; margin-top: 3px; }
  .letterhead .brand-tag { font-size: 7px; margin-top: 2px; }
  .letterhead .wave { bottom: 0; height: 150px; }
  .letterhead .footer-address { position: absolute; left: 26px; bottom: 28px; color: #fff; font-size: 9px; line-height: 1.4; }

  /* Disc */
  .disc { left: 593px; top: 36px; width: 264px; height: 264px; border-radius: 50%; background: var(--paper); }
  .disc .wave { top: 0; height: 264px; }
  .disc .brand { left: 50%; top: 24px; transform: translateX(-50%); align-items: center; }
  .disc .brand-dot { width: 12px; height: 12px; }
  .disc .brand-name { font-size: 14px; }
  .disc .brand-sub, .disc .brand-tag { font-size: 5px; margin-top: 2px; }
  .disc-hub { position: absolute; left: 92px; top: 92px; width: 80px; height: 80px; border-radius: 50%; background: var(--hole); border: 6px solid #d2d2d4; }
  .disc-hole { position: absolute; left: 120px; top: 120px; width: 24px; height: 24px; border-radius: 50%; background: var(--stage); }

  /* Business card front */
  .card-front { left: 619px; top: 365px; width: 250px; height: 144px; background: var(--paper); }
  .card-front .brand { left: 12px; top: 12px; }
  .card-front .brand-dot { width: 9px; height: 9px; }
  .card-front .brand-name { font-size: 11px; }
  .card-front .brand-sub, .card-front .brand-tag { font-size: 4px; margin-top: 1px; }
  .card-front .wave { bottom: 0; height: 48px; }
  .card-contact { position: absolute; left: 12px; top: 52px; font-size: 4.5px; line-height: 1.5; color: var(--ink); }
  .card-person { position: absolute; left: 148px; top: 62px; font-size: 5.5px; line-height: 1.4; }
  .card-person .person-name { font-weight: 700; color: var(--charcoal); }
  .card-person .person-role { color: var(--gold-deep); }

  /* Business card back */
  .card-back { left: 900px; top: 322px; width: 254px; height: 151px; background: var(--charcoal); }
  .card-map { position: absolute; left: 26px; top: 22px; width: 150px; height: 100px; background: linear-gradient(135deg, #6d6d6f, #7b7b7d); }
  .card-back .map-note { position: absolute; left: 150px; top: 68px; font-size: 5px; color: var(--gold); line-height: 1.4; }

  /* Envelope */
  .envelope { left: 643px; top: 540px; width: 485px; height: 226px; background: var(--paper); }
  .envelope .wave { top: 0; height: 130px; }
  .envelope .brand { left: 28px; top: 96px; }
  .envelope .brand-dot { width: 14px; height: 14px; }
  .envelope .brand-name { font-size: 17px; }
  .envelope .brand-sub, .envelope .brand-tag { font-size: 6px; margin-top: 2px; }
  .envelope .return-address { position: absolute; left: 28px; top: 150px; font-size: 7px; line-height: 1.4; color: var(--ink); }
</style>
</head>
<body>

<!-- Letterhead -->
<section class="piece letterhead">
  <div class="brand">
    <div class="brand-row"><span class="brand-dot"></span><span class="brand-name">OhelNoam</span></div>
    <span class="brand-sub">MESSIANIC CONGREGATION</span>
    <span class="brand-tag">Worship • Study • Fellowship</span>
  </div>
  <svg class="wave" viewBox="0 0 458 150" preserveAspectRatio="none" aria-hidden="true">
    <path d="M0 30 C120 -5 260 40 458 8 L458 22 C260 55 120 12 0 44 Z" fill="var(--gold)"/>
    <path d="M0 52 C130 24 270 62 458 30 L458 36 C270 70 130 32 0 58 Z" fill="var(--gold-deep)"/>
    <path d="M0 62 C140 36 280 76 458 40 L458 150 L0 150 Z" fill="var(--charcoal)"/>
  </svg>
  <p class="footer-address">5142 Callaway Lane<br>Orlando, FL 32867</p>
</section>

<!-- Disc -->
<section class="piece disc">
  <svg class="wave" viewBox="0 0 264 264" preserveAspectRatio="none" aria-hidden="true">
    <path d="M0 118 C70 100 160 150 264 104 L264 116 C160 162 70 112 0 130 Z" fill="var(--gold)"/>
    <path d="M0 136 C80 116 170 170 264 124 L264 264 L0 264 Z" fill="var(--charcoal)"/>
  </svg>
  <div class="brand">
    <div class="brand-row"><span class="brand-dot"></span><span class="brand-name">OhelNoam</span></div>
    <span class="brand-sub">MESSIANIC CONGREGATION</span>
    <span class="brand-tag">Worship • Study • Fellowship</span>
  </div>
  <div class="disc-hub"></div>
  <div class="disc-hole"></div>
</section>

<!-- Business card front -->
<section class="piece card-front">
  <div class="brand">
    <div class="brand-row"><span class="brand-dot"></span><span class="brand-name">OhelNoam</span></div>
    <span class="brand-sub">MESSIANIC CONGREGATION</span>
    <span class="brand-tag">Worship • Study • Fellowship</span>
  </div>
  <p class="card-contact">5142 Callaway Lane<br>Orlando, FL 32867<br>Tel 407.555.0148<br>gmorrow@ohelnoam.com<br>www.ohelnoam.com</p>
  <p class="card-person"><span class="person-name">Gregory T. Morrow</span><br><span class="person-role">Ro'i</span></p>
  <svg class="wave" viewBox="0 0 250 48" preserveAspectRatio="none" aria-hidden="true">
    <path d="M0 10 C70 0 150 24 250 4 L250 10 C150 30 70 6 0 16 Z" fill="var(--gold)"/>
    <path d="M0 20 C80 8 160 34 250 14 L250 48 L0 48 Z" fill="var(--charcoal)"/>
  </svg>
</section>

<!-- Business card back -->
<section class="piece card-back">
  <div class="card-map" role="img" aria-label="Street map showing the congregation location"></div>
  <p class="map-note">Find us here<br>5142 Callaway Lane</p>
</section>

<!-- Envelope -->
<section class="piece envelope">
  <svg class="wave" viewBox="0 0 485 130" preserveAspectRatio="none" aria-hidden="true">
    <path d="M0 0 L485 0 L485 60 C360 110 200 50 0 94 Z" fill="var(--charcoal)"/>
    <path d="M0 100 C200 58 360 116 485 68 L485 76 C360 124 200 66 0 108 Z" fill="var(--gold)"/>
  </svg>
  <div class="brand">
    <div class="brand-row"><span class="brand-dot"></span><span class="brand-name">OhelNoam</span></div>
    <span class="brand-sub">MESSIANIC CONGREGATION</span>
    <span class="brand-tag">Worship • Study • Fellowship</span>
  </div>
  <p class="return-address">5142 Callaway Lane<br>Orlando, FL 32867</p>
</section>

</body>
</html>
```